Corvalla Sponsored Content Images

Image spec: 1.91:1 ratio (1200x627px)We require 6x variations of this image: See the excel attached for the copy.Each image should contain the ZEMBO logo, 2 headshots if posible, a designed background and a CTA button + the copy.Please make sure that all of the copy is clear and big enough to read so it can be read on mobile devices.

Target Market(s)

This is for Corvalla ads to Executives of mid-market companies

Font styles to use
Sans Serif

Colors

Designer to choose colors to be used in the design.

```html
<!DOCTYPE html>
<html lang="en">
<head>
<meta charset="utf-8">
<title>ZEMBO Webinar Sponsored Content</title>
<link href="https://fonts.googleapis.com/css2?family=Roboto+Condensed:wght@400;700&display=swap" rel="stylesheet">
<style>
  :root {
    --stage: #222222;
    --navy: #1d3a6b;
    --navy-deep: #173260;
    --blue-bright: #2f6fd0;
    --blue-mid: #4a8ae0;
    --blue-light: #9cc3f0;
    --panel: rgba(236, 236, 250, 0.9);
    --orange-top: #fcb23a;
    --orange-bottom: #f48b1c;
    --ring: rgba(200, 208, 230, 0.85);
    --photo-dark: #4d5156;
    --photo-light: #cfd3d6;
  }
  * { box-sizing: border-box; margin: 0; padding: 0; }
  html, body { width: 998px; height: 1200px; overflow: hidden; background: var(--stage); }
  body { position: relative; font-family: "Roboto Condensed", "Arial Narrow", sans-serif; color: var(--navy); }

  .ad-banner {
    position: absolute; width: 896px; height: 467px; overflow: hidden;
    background:
      radial-gradient(ellipse at 55% 75%, var(--blue-light) 0%, transparent 45%),
      linear-gradient(135deg, var(--blue-bright) 0%, var(--blue-mid) 45%, var(--blue-bright) 100%);
  }
  .ad-banner--first { left: 46px; top: 103px; }
  .ad-banner--second { left: 57px; top: 630px; }

  .content-panel {
    position: absolute; left: 52px; top: 39px; width: 792px; height: 388px;
    background: linear-gradient(160deg, rgba(245,245,252,0.95), var(--panel) 60%, rgba(220,226,245,0.92));
    box-shadow: 0 2px 6px rgba(10,30,70,0.55);
    border: 1px solid rgba(30,50,90,0.5);
  }

  .event-date { position: absolute; left: 82px; top: 57px; width: 110px; text-align: center; font-weight: 700; line-height: 1.05; }
  .event-date__day { font-size: 24px; }
  .event-date__day sup { font-size: 12px; }
  .event-date__weekday { font-size: 17px; }
  .event-date__time { font-size: 24px; margin-top: 4px; }

  .brand-name { position: absolute; right: 72px; top: 76px; font-size: 42px; font-weight: 400; color: var(--navy); letter-spacing: 1px; }

  .speaker-ring {
    position: absolute; left: 395px; top: 28px; width: 196px; height: 196px; border-radius: 50%;
    background: var(--ring);
  }
  .speaker-photo {
    position: absolute; left: 403px; top: 36px; width: 180px; height: 180px; border-radius: 50%;
    border: 2px solid var(--navy);
    background: radial-gradient(circle at 50% 35%, var(--photo-light) 0%, #a99a8c 35%, var(--photo-dark) 70%);
  }

  .format-pill {
    position: absolute; left: 278px; top: 201px; width: 324px; height: 60px; border-radius: 30px;
    background: linear-gradient(var(--orange-top), var(--orange-bottom));
    box-shadow: 0 0 0 7px var(--ring), 0 4px 6px rgba(0,0,0,0.25);
    display: flex; align-items: center; justify-content: center;
    font-weight: 700; font-size: 32px; color: var(--navy);
  }
  .ad-banner--second .format-pill { font-size: 27px; }

  .webinar-title { position: absolute; left: 0; right: 0; top: 278px; text-align: center; font-weight: 700; font-size: 32px; }

  .webinar-subtitle {
    position: absolute; top: 331px; left: 139px; width: 620px; height: 49px;
    border-top: 2px solid var(--navy); border-bottom: 2px solid var(--navy);
    display: flex; align-items: center; justify-content: center;
    font-weight: 700; font-size: 29px; white-space: nowrap;
  }
  .ad-banner--second .webinar-subtitle { left: 80px; width: 726px; font-size: 25px; }

  .cta-button {
    position: absolute; left: 300px; top: 399px; width: 252px; height: 50px; border-radius: 25px;
    background: linear-gradient(var(--navy), var(--navy-deep));
    box-shadow: 0 0 0 6px var(--ring), 0 3px 5px rgba(0,0,0,0.3);
    display: flex; align-items: center; justify-content: center;
    color: #ffffff; font-weight: 700; font-size: 25px;
  }
  .ad-banner--second .cta-button { font-size: 21px; }
</style>
</head>
<body>
  <section class="ad-banner ad-banner--first" role="img" aria-label="Blue circuit board background">
    <div class="content-panel"></div>
    <div class="event-date">
      <div class="event-date__day">JUNE 12<sup>th</sup></div>
      <div class="event-date__weekday">WEDNESDAY</div>
      <div class="event-date__time">1PM</div>
    </div>
    <div class="brand-name">ZEMBO</div>
    <div class="speaker-ring"></div>
    <div class="speaker-photo" role="img" aria-label="Headshot of the webinar speaker"></div>
    <div class="format-pill">FREE Live Webinar</div>
    <h2 class="webinar-title">“Cybersecurity Starts at the Top”</h2>
    <p class="webinar-subtitle">How to 'sell' a cybersecurity strategy internally</p>
    <div class="cta-button">BOOK YOUR PLACE</div>
  </section>

  <section class="ad-banner ad-banner--second" role="img" aria-label="Blue circuit board background">
    <div class="content-panel"></div>
    <div class="event-date">
      <div class="event-date__day">JUNE 12<sup>th</sup></div>
      <div class="event-date__weekday">WEDNESDAY</div>
      <div class="event-date__time">1PM</div>
    </div>
    <div class="brand-name">ZEMBO</div>
    <div class="speaker-ring"></div>
    <div class="speaker-photo" role="img" aria-label="Headshot of the webinar speaker"></div>
    <div class="format-pill">Munch &amp; Learn Webina</div>
    <h2 class="webinar-title">“Cybersecurity Starts at the Top”</h2>
    <p class="webinar-subtitle">Your step-by step guide to implementing a cybersecurity strategy</p>
    <div class="cta-button">RESERVE YOUR PLACE</div>
  </section>
</body>
</html>
```